Redesign Home Page

We need a new home page with a white background. Our company provides singing instruction to students world wide, both in person and on line. We're looking for a very clean and open design with maximum white space. The main goal of the page will be to get users to sign up for our mailing list. The current site is www.kelvarsong.com. I think the new page can be a long page (scrolll down is ok), to allow for more white space while still using the text from the current page.
Updates

Project Deadline Extended
Reason: Hello to all Designers, I apologize for not giving feedback this weekend. We went out of town for the Memorial Day holiday and I had no internet. I will be extending the deadline to Thursday. -Marcus

Target Market(s)

Singers of all ages and abilities, especially beginners.

Industry/Entity Type

It Company

Requirements
Must have
• 1. A white background
2. Lots of open space
3. An email sign up form on the top right that reads:
a. “Improve Your Singing Now.
b. Sign up for our Free Video Series: Tone Pathway
4. Testimonails: found on https://www.kelvarsong.com/tone-ascent
5. My logo with the piano
6. My photo
7. Learn about our Lessons in:
a. San Francisco
b. Alameda
8. On Line Programs:
a. Tone Ascent
b. Zelvo Lessons

Nice to have
• Link to current student page: http://kelvarsong.com/what-students-say/students2
Pictures of singers
Video box: Use Marcus_Example
Should not have
• See "KelvarSong Redesign" file for more details.

```html
<!DOCTYPE html>
<html lang="en">
<head>
<meta charset="utf-8">
<title>Marcus Halden School of Voice</title>
<link rel="stylesheet" href="https://fonts.googleapis.com/css2?family=Oxygen:wght@300;400;700&display=swap">
<style>
:root{
  --blue:#27a9e1;
  --band:#0aa4dc;
  --band-card:#3bbce8;
  --navy:#0f4a6b;
  --dark:#1e1e1e;
  --text:#222;
  --muted:#8a8a8a;
  --line:#e2e2e2;
  --soft:#f8f8f8;
  --orange:#f7891c;
  --white:#fff;
}
*{box-sizing:border-box;margin:0;padding:0}
html,body{width:1200px;height:2177px;overflow:hidden;background:var(--white)}
body{position:relative;font-family:'Oxygen',Arial,sans-serif;color:var(--text)}
.abs{position:absolute}

/* header */
.brand{left:112px;top:32px;display:flex;align-items:center;gap:12px}
.brand-mark{width:60px;height:52px;border:3px solid var(--blue);border-radius:8px}
.brand-name{font-size:30px;font-weight:700;color:#555;line-height:1}
.brand-tag{font-size:13px;color:#555;margin-top:3px;padding-left:20px}
.account{right:130px;top:12px;font-size:15px;display:flex;gap:8px;align-items:center}
.account a{text-decoration:none;color:var(--text)}
.account .register{color:var(--blue)}

.nav{left:0;top:116px;width:1200px;height:48px;background:var(--dark)}
.nav ul{list-style:none;display:flex;height:48px;padding-left:127px}
.nav li{color:var(--white);font-size:14px;text-transform:uppercase;line-height:48px;padding:0 20px;border-right:1px solid #444;position:relative}
.nav li:last-child{border-right:0}
.nav li.active:after{content:"";position:absolute;left:50%;bottom:0;margin-left:-6px;border:6px solid transparent;border-bottom-color:var(--white)}

/* hero */
.hero{left:0;top:164px;width:1200px;height:460px;background:linear-gradient(90deg,#e8e8e8 0%,#cfcfcf 30%,#5a5a5a 45%,#2a2a2a 62%,#9a9a9a 80%,#6a6a6a 100%)}
.hero-kicker{left:116px;top:300px;font-size:28px;font-weight:300}
.hero-title{left:116px;top:340px;font-size:42px;font-weight:400}
.hero-copy{left:118px;top:396px;width:370px;font-size:13px;line-height:21px;color:#666}
.dots{left:118px;top:450px;display:flex;gap:4px}
.dots span{width:14px;height:14px;border-radius:50%;background:#111}
.dots span:first-child{background:var(--blue)}

.signup{left:773px;top:221px;width:313px;height:314px;background:var(--blue);color:var(--white);text-align:center;padding-top:30px}
.signup .eyebrow{font-size:16px}
.signup h2{font-size:25px;font-weight:400;line-height:33px;margin-top:8px}
.signup .field{display:block;margin:14px auto 0;width:262px;height:30px;background:#1e96cb;border:1px solid #5cc2ec;font-size:12px;color:var(--white);text-align:left;padding:8px 14px}
.signup .field+.field{margin-top:10px}
.signup .go{display:block;margin:14px auto 0;width:256px;height:45px;background:var(--navy);font-size:20px;line-height:45px;color:var(--white);border-radius:3px}

/* about */
.section-title{width:1200px;left:0;text-align:center;font-size:34px;font-weight:300}
.section-lead{left:170px;width:860px;text-align:center;font-size:13px;line-height:21px;color:var(--muted)}
.cards{display:flex;border:1px solid var(--line);border-radius:4px}
.card{flex:1;display:flex;gap:16px;padding:22px;border-right:1px solid var(--line)}
.card:last-child{border-right:0}
.card-photo{width:132px;height:116px;flex:none}
.card h3{font-size:26px;font-weight:400;color:var(--blue);line-height:1;margin-top:2px}
.card p{font-size:12px;line-height:21px;color:#555;margin-top:8px}
.card .more{font-size:12px;font-weight:700;text-transform:uppercase;margin-top:2px}

.band{left:0;top:1005px;width:1200px;height:385px;background:var(--band);color:var(--white)}
.band .cards{border-color:#7dd3f2;background:var(--band-card)}
.band .card{border-color:#7dd3f2}
.band .card h3,.band .card p,.band .card .more{color:var(--white)}

/* feature */
.feature{left:0;top:1390px;width:1200px;height:393px;background:var(--soft)}
.feature h2{left:140px;top:62px;font-size:30px;font-weight:300}
.feature .lead{left:144px;top:104px;width:530px;font-size:12px;line-height:21px;color:#555}
.ticks{left:144px;top:152px;list-style:none}
.ticks li{font-size:14px;height:30px;display:flex;align-items:center;gap:8px;color:#333}
.cta{left:141px;top:284px;width:151px;height:40px;background:var(--orange);color:var(--white);font-size:14px;font-weight:700;line-height:40px;text-align:center;border-radius:3px}
.video{left:711px;top:68px;width:348px;height:231px;background:var(--white);border:1px solid #ddd;padding:6px;box-shadow:0 1px 3px rgba(0,0,0,.15)}
.video-screen{width:100%;height:100%;background:linear-gradient(160deg,#3a4456,#151a22);position:relative}
.video-screen svg{position:absolute;left:50%;top:50%;margin:-36px 0 0 -36px}

/* testimonials */
.quote-title{left:0;width:1200px;top:1830px;text-align:center;font-size:34px;font-weight:300;color:var(--blue)}
.quote{left:210px;top:1880px;width:780px;text-align:center;font-size:13px;line-height:21px;font-style:italic;color:var(--muted)}
.author{left:0;width:1200px;top:1972px;text-align:center;font-size:15px;font-weight:700;color:#444}

/* footer */
.footer{left:0;top:2052px;width:1200px;height:125px;background:var(--dark);color:var(--white)}
.footer-links{left:122px;top:36px;font-size:13px;font-weight:700;text-transform:uppercase}
.footer-links span{margin:0 8px}
.copyright{left:122px;top:66px;font-size:12px;color:#ccc}
.social{left:962px;top:30px;display:flex;gap:3px}
.social span{width:28px;height:28px;border-radius:50%;background:var(--white)}
</style>
</head>
<body>

<header>
  <div class="abs brand">
    <span class="brand-mark"></span>
    <div>
      <div class="brand-name">MarcusHalden</div>
      <div class="brand-tag">School of Voice</div>
    </div>
  </div>
  <div class="abs account">
    <svg width="16" height="16" viewBox="0 0 16 16"><circle cx="8" cy="4.5" r="3.5" fill="#27a9e1"/><path d="M1 16c0-5 3-7 7-7s7 2 7 7z" fill="#27a9e1"/></svg>
    <a class="register" href="#">Register</a> / <a href="#">Sign In</a>
  </div>
  <nav class="abs nav">
    <ul>
      <li class="active">Home</li>
      <li>Voice Lessons</li>
      <li>Blog</li>
      <li>What Students Say</li>
      <li>Meet the Instructors</li>
      <li>Tone Ascent</li>
    </ul>
  </nav>
</header>

<section class="abs hero" role="img" aria-label="Black and white portrait of the voice instructor smiling"></section>
<div class="abs hero-kicker">Phasellus dolor Sceleris</div>
<div class="abs hero-title">Donec convallis pede</div>
<p class="abs hero-copy">Maecenas at justo id velit placerat molestie Donec dictum lectus non odio Cras a ante vitae enim iaculis aliquam</p>
<div class="abs dots"><span></span><span></span><span></span><span></span></div>

<form class="abs signup">
  <div class="eyebrow">Improve Your Singing Now</div>
  <h2>Sign up for our Free<br>Video Series</h2>
  <span class="field">Your Name</span>
  <span class="field">Email address</span>
  <span class="go">Get Started</span>
</form>

<h2 class="abs section-title" style="top:668px">About Our Lessons</h2>
<p class="abs section-lead" style="top:720px">Phasellus felis dolor scelerisque a tempus eget lobortis id libero Aliquam nec erat at purus cursus interdum Vestibulum ligula augue bibendum accumsan vestibulum ut commodo a mi Morbi ornare gravida elit Integer congue augue et malesuada iaculis ipsum dui aliquet felis</p>
<div class="abs cards" style="left:190px;top:792px;width:836px;height:171px">
  <article class="card">
    <div class="card-photo" role="img" aria-label="Red suspension bridge over the bay" style="background:linear-gradient(180deg,#9cc3e6,#b34a2c 60%,#5a5a52)"></div>
    <div><h3>San Francisco</h3><p>Phasellus felis dolor scelerisque a tempus eget lobortis id libero Aliquam nec erat at purus cursus interdum Vestibulum ligula</p><div class="more">Learn More</div></div>
  </article>
  <article class="card">
    <div class="card-photo" role="img" aria-label="City skyline of Alameda" style="background:linear-gradient(180deg,#a9cbe8,#7b8795 55%,#3e4651)"></div>
    <div><h3>Alameda</h3><p>Phasellus felis dolor scelerisque a tempus eget lobortis id libero Aliquam nec erat at purus cursus interdum Vestibulum ligula</p><div class="more">Learn More</div></div>
  </article>
</div>

<section class="abs band">
  <h2 class="abs section-title" style="top:48px">On Line Programs</h2>
  <p class="abs section-lead" style="top:96px;color:#dff3fb">Phasellus felis dolor scelerisque a tempus eget lobortis id libero Aliquam nec erat at purus cursus interdum Vestibulum ligula augue</p>
  <div class="abs cards" style="left:192px;top:136px;width:836px;height:172px">
    <article class="card">
      <div class="card-photo" role="img" aria-label="Student wearing headphones listening to a lesson" style="background:linear-gradient(135deg,#d9c8b4,#6a5242 60%,#b4bcc4)"></div>
      <div><h3>Tone Ascent</h3><p>Phasellus felis dolor scelerisque a tempus eget lobortis id libero Aliquam nec erat at purus cursus interdum Vestibulum</p><div class="more">Learn More</div></div>
    </article>
    <article class="card">
      <div class="card-photo" role="img" aria-label="Man in shirt and tie waving during a video call" style="background:linear-gradient(135deg,#e3e7ec,#8fa5bc 55%,#3e4b5c)"></div>
      <div><h3>Zelvo Lessons</h3><p>Phasellus felis dolor scelerisque a tempus eget lobortis id libero Aliquam nec erat at purus cursus interdum Vestibulum</p><div class="more">Learn More</div></div>
    </article>
  </div>
</section>

<section class="abs feature">
  <h2 class="abs">Tone Ascent Available Now</h2>
  <p class="abs lead">Phasellus felis dolor scelerisque a tempus eget lobortis id libero Aliquam nec erat at purus cursus interdum Vestibulum ligula augue bibendum accumsan vest</p>
  <ul class="abs ticks">
    <li><svg width="16" height="14" viewBox="0 0 16 14"><path d="M1 7l5 5L15 1" fill="none" stroke="#27a9e1" stroke-width="3"/></svg>Get Instant Access</li>
    <li><svg width="16" height="14" viewBox="0 0 16 14"><path d="M1 7l5 5L15 1" fill="none" stroke="#27a9e1" stroke-width="3"/></svg>Unique methods that are ideal for voice health</li>
    <li><svg width="16" height="14" viewBox="0 0 16 14"><path d="M1 7l5 5L15 1" fill="none" stroke="#27a9e1" stroke-width="3"/></svg>The Most Advanced Platform for On Line Singing Instruction</li>
    <li><svg width="16" height="14" viewBox="0 0 16 14"><path d="M1 7l5 5L15 1" fill="none" stroke="#27a9e1" stroke-width="3"/></svg>60+ Videos and Audio Workouts</li>
  </ul>
  <div class="abs cta">GET STARTED</div>
  <div class="abs video">
    <div class="video-screen" role="img" aria-label="Tone Ascent lesson video player">
      <svg width="72" height="72" viewBox="0 0 72 72"><circle cx="36" cy="36" r="33" fill="none" stroke="#fff" stroke-width="4"/><path d="M28 21l23 15-23 15z" fill="#fff"/></svg>
    </div>
  </div>
</section>

<h2 class="abs quote-title">Testimonials</h2>
<p class="abs quote">Maecenas at justo id velit placerat molestie Donec dictum lectus non odio Cras a ante vitae enim iaculis aliquam Mauris nunc quam venenatis nec euismod sit amet egestas placerat est Pellentesque habitant morbi tristique senectus et netus et malesuada fames ac turpis egestas Cras id elit Integer quis urna Ut ante enim dapibus malesuada fringilla eu condimentum quis tellus Aenean porttitor eros vel dolor Donec convallis pede venenatis nibh Duis quam Nam eget lacus</p>
<div class="abs author">By Author Name</div>

<footer class="abs footer">
  <div class="abs footer-links">Home<span>|</span>Voice Lessons<span>|</span>Blog<span>|</span>What Students Say<span>|</span>Meet the Instructors<span>|</span>Tone Ascent</div>
  <div class="abs copyright">© 2014 Company Name &nbsp;All right reserved &nbsp;Term of Use</div>
  <div class="abs social"><span></span><span></span><span></span><span></span></div>
</footer>

</body>
</html>
```